A Hair, Beauty and Nails Wholesalers Needs a Business Card Design

We need a business card design for our company which is being passed from parents to daughter, so we wont to re-launch the company with an updated, modern, sophisticated, elegant, chic and fresh look which still incorporates the original colour scheme of Hot Pink, Dark Grey and White. The original logo which is attached can be used on the card but we would like to see some designs with the logo and some without, as we have not yet decided if we want the logo on the card. The name of our company is 'Velmora Supplies' and the name of our website is VelmoraGlowandPolish.example.au. We specialise in supplying a massive range of Hair, Beauty and Nail products to the industry. We are based in QLD, Australia but ship many orders via our website all across Australia.

```html
<!DOCTYPE html>
<html lang="en">
<head>
<meta charset="utf-8">
<title>Velmora Supplies – Business Card</title>
<link href="https://fonts.googleapis.com/css2?family=Montserrat:wght@400;500;600&display=swap" rel="stylesheet">
<style>
  :root {
    --hot-pink: #e10886;
    --dark-grey: #4a4a48;
    --band-grey: #6b6a66;
    --white: #ffffff;
    --page: #ffffff;
  }
  html, body {
    margin: 0;
    padding: 0;
    width: 1200px;
    height: 1000px;
    overflow: hidden;
    background: var(--page);
    font-family: "Montserrat", sans-serif;
  }
  .canvas {
    position: relative;
    width: 1200px;
    height: 1000px;
  }
  .card {
    position: absolute;
    left: 324px;
    width: 550px;
    height: 339px;
    box-shadow: 0 0 18px rgba(0, 0, 0, 0.12);
    overflow: hidden;
  }
  .card--front {
    top: 125px;
    background: var(--hot-pink);
  }
  .card--back {
    top: 533px;
    background: var(--white);
  }
  .brand {
    position: absolute;
    display: flex;
    align-items: center;
    gap: 10px;
  }
  .brand__dot {
    width: 58px;
    height: 58px;
    border-radius: 50%;
    flex: none;
  }
  .brand__name {
    font-weight: 600;
    font-size: 25px;
    letter-spacing: 0.2px;
    white-space: nowrap;
  }
  .card--front .brand {
    left: 124px;
    top: 140px;
  }
  .card--front .brand__dot { background: var(--white); }
  .card--front .brand__name { color: var(--white); }
  .card--back .brand {
    left: 68px;
    top: 51px;
  }
  .card--back .brand__dot { background: var(--hot-pink); }
  .card--back .brand__name { color: var(--dark-grey); }
  .contact {
    position: absolute;
    right: 59px;
    top: 176px;
    text-align: right;
    color: var(--dark-grey);
  }
  .contact__company {
    margin: 0;
    font-size: 20px;
    font-weight: 500;
    letter-spacing: 0.5px;
    line-height: 28px;
  }
  .contact__address {
    margin: 2px 0 0;
    font-size: 13.5px;
    font-weight: 400;
    line-height: 22px;
  }
  .contact__lines {
    margin: 2px 0 0;
    font-size: 17px;
    font-weight: 500;
    line-height: 24px;
  }
  .web-band {
    position: absolute;
    left: 0;
    bottom: 0;
    width: 100%;
    height: 70px;
    background: var(--band-grey);
  }
  .web-band__url {
    position: absolute;
    right: 59px;
    top: 14px;
    margin: 0;
    color: var(--white);
    font-size: 17.5px;
    font-weight: 600;
  }
</style>
</head>
<body>
<main class="canvas">
  <section class="card card--front" aria-label="Card front">
    <div class="brand">
      <span class="brand__dot"></span>
      <span class="brand__name">Velmora Supplies</span>
    </div>
  </section>

  <section class="card card--back" aria-label="Card back">
    <div class="brand">
      <span class="brand__dot"></span>
      <span class="brand__name">Velmora Supplies</span>
    </div>
    <div class="contact">
      <p class="contact__company">VELMORA SUPPLIES</p>
      <p class="contact__address">58 Carrow Lane, BRINDALE QLD 4399 Australia</p>
      <p class="contact__lines">07 5550 0123 • info@velmoraglowandpolish.example.au</p>
    </div>
    <div class="web-band">
      <p class="web-band__url">www.VelmoraGlowandPolish.example.au</p>
    </div>
  </section>
</main>
</body>
</html>
```